Postcard Design

See website www.oakbrim-vitalcare.com. Need mailout to patients of a doctor who is leaving (Dr. KdMorrow), to market doctor staying (Dr Danvers) to retain patients in the practice (Crestmoor Heart Group) at two different locations (Pace, FL and West Pensacola). Use some of the graphics in the web design and content, plus reassurances to patients that their care will continue at that location by Dr Danvers

Doctor

```html
<!DOCTYPE html>
<html lang="en">
<head>
<meta charset="utf-8">
<title>Crestmoor Heart Group Postcard</title>
<link href="https://fonts.googleapis.com/css2?family=Cinzel:wght@600;700&family=Open+Sans:wght@400;600;700&display=swap" rel="stylesheet">
<style>
  :root {
    --stage: #3a3a3a;
    --card: #ffffff;
    --red: #c8262c;
    --red-dark: #9e1a20;
    --slate: #2f4a50;
    --ink: #4a4a4a;
    --grey-soft: #e6e6e6;
    --photo-light: #dfe7c9;
    --photo-mid: #9fb07a;
    --photo-deep: #5d6e46;
  }
  * { margin: 0; padding: 0; box-sizing: border-box; }
  html, body { width: 900px; height: 1200px; overflow: hidden; }
  body { background: var(--stage); font-family: "Open Sans", Arial, sans-serif; position: relative; }

  .postcard { position: absolute; left: 45px; width: 810px; background: var(--card); overflow: hidden; box-shadow: 0 6px 18px rgba(0,0,0,.45); }
  .postcard--front { top: 24px; height: 570px; }
  .postcard--back { top: 630px; height: 540px; }

  .brand { position: absolute; display: flex; align-items: center; gap: 10px; color: var(--red); font-weight: 700; font-size: 24px; letter-spacing: .3px; }
  .brand__dot { width: 20px; height: 20px; border-radius: 50%; background: var(--red); }
  .postcard--front .brand { left: 36px; top: 44px; }
  .postcard--back .brand { left: 40px; top: 48px; }

  .art { position: absolute; inset: 0; }

  .doctor-name { position: absolute; left: 22px; top: 338px; width: 210px; padding: 8px 14px; background: var(--slate); color: #fff; font-family: "Cinzel", serif; font-size: 15px; line-height: 1.3; }

  .headline { position: absolute; left: 330px; top: 312px; width: 460px; font-family: "Cinzel", serif; font-weight: 700; line-height: 1.15; }
  .headline__leaving { color: var(--red); font-size: 28px; }
  .headline__staying { color: var(--red-dark); font-size: 28px; margin-top: 2px; }

  .care-banner { position: absolute; left: 322px; top: 452px; width: 468px; height: 44px; border-radius: 10px; background: var(--red); color: #fff; font-family: "Cinzel", serif; font-weight: 700; font-size: 14.5px; white-space: nowrap; display: flex; align-items: center; justify-content: center; letter-spacing: .2px; }

  .bio { position: absolute; left: 40px; top: 120px; width: 350px; font-size: 12.5px; line-height: 1.55; color: var(--ink); }
  .divider { position: absolute; left: 420px; top: 40px; width: 1px; height: 380px; background: #cfcfcf; }
  .stamp { position: absolute; right: 40px; top: 40px; width: 80px; height: 90px; border: 2px solid #333; }
  .address-line { position: absolute; left: 470px; width: 300px; height: 1px; background: #bdbdbd; }
</style>
</head>
<body>

<section class="postcard postcard--front">
  <svg class="art" width="810" height="570" viewBox="0 0 810 570">
    <defs>
      <linearGradient id="outdoorPhoto" x1="0" y1="0" x2="1" y2="1">
        <stop offset="0" stop-color="#dfe7c9"/>
        <stop offset=".55" stop-color="#9fb07a"/>
        <stop offset="1" stop-color="#5d6e46"/>
      </linearGradient>
      <linearGradient id="portraitPhoto" x1="0" y1="0" x2="0" y2="1">
        <stop offset="0" stop-color="#d9dcdf"/>
        <stop offset="1" stop-color="#8c949b"/>
      </linearGradient>
    </defs>
    <path d="M300 0 H810 V300 H330 Q300 200 300 0 Z" fill="url(#outdoorPhoto)" role="img" aria-label="Photo of a smiling senior couple walking hand in hand outdoors in sunlight"/>
    <circle cx="128" cy="230" r="104" fill="none" stroke="#c8262c" stroke-width="10"/>
    <circle cx="128" cy="230" r="96" fill="url(#portraitPhoto)" role="img" aria-label="Portrait photo of the cardiologist in a white coat"/>
    <path d="M0 470 Q240 430 420 560 L420 570 H0 Z" fill="#c8262c"/>
    <path d="M0 500 Q220 470 360 570 H0 Z" fill="#9e1a20"/>
  </svg>

  <div class="brand"><span class="brand__dot"></span>Crestmoor Heart Group</div>

  <div class="doctor-name">Martin J. Danvers,<br>MD FACC</div>

  <h1 class="headline">
    <div class="headline__leaving">Dr. KdMorrow is leaving to market doctor</div>
    <div class="headline__staying">Dr. Danvers is staying</div>
  </h1>

  <div class="care-banner">Care will continue at that location by Dr Danvers</div>
</section>

<section class="postcard postcard--back">
  <svg class="art" width="810" height="540" viewBox="0 0 810 540">
    <defs>
      <linearGradient id="couplePhoto" x1="0" y1="0" x2="1" y2="1">
        <stop offset="0" stop-color="#e8e2da"/>
        <stop offset="1" stop-color="#9a8f86"/>
      </linearGradient>
    </defs>
    <path d="M0 420 Q400 380 810 500 V540 H0 Z" fill="#e6e6e6"/>
    <path d="M0 470 Q160 420 300 540 H0 Z" fill="#c8262c"/>
    <circle cx="140" cy="440" r="86" fill="#fff"/>
    <circle cx="140" cy="440" r="80" fill="url(#couplePhoto)" role="img" aria-label="Photo of a happy senior couple smiling together"/>
  </svg>

  <div class="brand"><span class="brand__dot"></span>Crestmoor Heart Group</div>

  <p class="bio">Dr. Danvers is a cardiologist with the Crestmoor Heart Group in Larkfield, Ohio, with a special interest in Senior Cardiology. He earned his medical degree from Halvern University Medical School. His postgraduate training included a residency in internal medicine at Halvern and a cardiology fellowship at Sorrelby University Medical School in Ashford. He is board certified in cardiology, internal medicine, and clinical lipidology.</p>

  <div class="divider"></div>
  <div class="stamp"></div>
  <div class="address-line" style="top:230px"></div>
  <div class="address-line" style="top:270px"></div>
  <div class="address-line" style="top:310px"></div>
  <div class="address-line" style="top:350px"></div>
</section>

</body>
</html>
```